New Business Card Design for Engineering and Surveying Company

We need a new design template for our business cards. We are a civil engineering, land surveying and pipeline integrity business. Please see dkhpartners.com for details. We need a bold, new business card design to complement our rebranding and marketing program. We have anew logo and attached vectro file. Please find additional details below. I am available to answer any questions.

Target Market(s)

Contractors, business owners, oil companies

Contact Information for Business Card

Needs to be customizable for different people (name, title, cell)

Font styles to use
Sans Serif
Other font styles liked:
• See eps file

Requirements
Must have
• Example Information:
Trevor Ashcombe

T:409-555-0173
M: 202-555-0148
tashcombe@dkhprtnrs.com

Address: 1875 Pinecrest Parkway, Beaumont, Texas 77703
Email: tolvanrey@dkhpartners.com
Website: www.dkhpartners.com
Nice to have
• I would like the back of the card to have the logo on a bold background with the text below:

[logo]
DORAN KESSLING & PARTNERS
CIVIL ENGINEERING | LAND SURVEYING | PIPELINE INTEGRITY

The reverse side should have the contact information for the person (example above), a smaller version of the logo and a graphic

```html
<!DOCTYPE html>
<html lang="en">
<head>
<meta charset="utf-8">
<title>Doran Kessling &amp; Partners – Business Card</title>
<link href="https://fonts.googleapis.com/css2?family=Mulish:wght@400;500;800;900&display=swap" rel="stylesheet">
<style>
  :root {
    --bg: #8f8f8f;
    --card: #000000;
    --red: #e8202e;
    --white: #ffffff;
    --text: #f2f2f2;
  }
  * { margin: 0; padding: 0; box-sizing: border-box; }
  html, body {
    width: 1200px; height: 960px; overflow: hidden;
    background: var(--bg);
    font-family: "Mulish", "Helvetica Neue", Arial, sans-serif;
  }
  .canvas { position: relative; width: 1200px; height: 960px; }
  .card {
    position: absolute; left: 281px; width: 655px; height: 373px;
    background: var(--card); border-radius: 26px; overflow: hidden;
    color: var(--text);
  }
  .card--front { top: 59px; }
  .card--back { top: 501px; }

  .brand { position: absolute; display: flex; align-items: center; gap: 14px; }
  .brand__dot { border-radius: 50%; background: var(--red); flex: none; }
  .brand__name { color: var(--white); font-weight: 900; letter-spacing: 1px; line-height: 1; }

  .card--front .brand { right: 43px; top: 88px; }
  .card--front .brand__dot { width: 34px; height: 34px; }
  .card--front .brand__name { font-size: 60px; }

  .person { position: absolute; left: 52px; top: 177px; }
  .person__name { color: var(--red); font-size: 24px; font-weight: 500; line-height: 30px; }
  .person__title { font-size: 17.5px; line-height: 22px; }

  .contact-list { position: absolute; list-style: none; font-size: 16.5px; }
  .contact-list li { display: flex; align-items: center; height: 22.5px; }
  .contact-list .icon { width: 13px; height: 13px; margin-right: 9px; flex: none; fill: var(--red); }
  .contact-list--personal { left: 52px; top: 256px; }
  .contact-list--office { left: 398px; top: 280px; }

  .address { position: absolute; left: 392px; top: 220px; font-size: 16.5px; line-height: 22.5px; }

  .card--back .brand { left: 0; right: 0; top: 150px; justify-content: center; gap: 20px; }
  .card--back .brand__dot { width: 52px; height: 52px; }
  .card--back .brand__name { font-size: 84px; }
  .back__company {
    position: absolute; left: 0; right: 0; top: 272px; text-align: center;
    color: var(--red); font-size: 17px; letter-spacing: 0.2px;
  }
  .back__services {
    position: absolute; left: 0; right: 0; top: 298px; text-align: center;
    color: var(--white); font-size: 17px; letter-spacing: 0.2px;
  }
</style>
</head>
<body>
<div class="canvas">

  <section class="card card--front">
    <div class="brand">
      <span class="brand__dot"></span>
      <span class="brand__name">DKH</span>
    </div>

    <div class="person">
      <div class="person__name">Trevor Ashcombe</div>
      <div class="person__title">Manager</div>
    </div>

    <ul class="contact-list contact-list--personal">
      <li>
        <svg class="icon" viewBox="0 0 16 16"><path d="M3.5 1 6 4 4.6 5.8c.9 2 2.6 3.8 4.6 4.7L11 9l3 2.5-1.6 2.8C7 14 2 9 1.5 3.2z"/></svg>
        409-555-0173
      </li>
      <li>
        <svg class="icon" viewBox="0 0 16 16"><path d="M4.5 0h7A1.5 1.5 0 0 1 13 1.5v13a1.5 1.5 0 0 1-1.5 1.5h-7A1.5 1.5 0 0 1 3 14.5v-13A1.5 1.5 0 0 1 4.5 0zM5 2v10h6V2zm3 11a1 1 0 1 0 0 2 1 1 0 0 0 0-2z"/></svg>
        202-555-0148
      </li>
      <li>
        <svg class="icon" viewBox="0 0 16 16"><path d="M1 3.5h14v9H1zm1.5 1.3v.3L8 9l5.5-3.9v-.3zM2.5 6.7v4.5h11V6.7L8 10.6z"/></svg>
        tashcombe@dkhprtnrs.com
      </li>
    </ul>

    <div class="address">
      1875 Pinecrest Parkway<br>
      Larkwood, Texas 77390
    </div>

    <ul class="contact-list contact-list--office">
      <li>
        <svg class="icon" viewBox="0 0 16 16"><path d="M1 3.5h14v9H1zm1.5 1.3v.3L8 9l5.5-3.9v-.3zM2.5 6.7v4.5h11V6.7L8 10.6z"/></svg>
        tolvanrey@dkhpartners.com
      </li>
      <li>
        <svg class="icon" viewBox="0 0 16 16"><path d="M8 1a7 7 0 1 0 0 14A7 7 0 0 0 8 1zm-1 1.6C5.9 3.8 5.3 5.4 5.2 7.3H2.6A5.5 5.5 0 0 1 7 2.6zm2 0a5.5 5.5 0 0 1 4.4 4.7h-2.6c-.1-1.9-.7-3.5-1.8-4.7zM8 2.9c1 1.1 1.6 2.6 1.7 4.4H6.3C6.4 5.5 7 4 8 2.9zM2.6 8.7h2.6c.1 1.9.7 3.5 1.8 4.7a5.5 5.5 0 0 1-4.4-4.7zm3.7 0h3.4C9.6 10.5 9 12 8 13.1 7 12 6.4 10.5 6.3 8.7zm4.5 0h2.6A5.5 5.5 0 0 1 9 13.4c1.1-1.2 1.7-2.8 1.8-4.7z"/></svg>
        www.dkhpartners.com
      </li>
    </ul>
  </section>

  <section class="card card--back">
    <div class="brand">
      <span class="brand__dot"></span>
      <span class="brand__name">DKH</span>
    </div>
    <div class="back__company">DORAN KESSLING &amp; PARTNERS</div>
    <div class="back__services">CIVIL ENGINEERING | LAND SURVEYING | PIPELINE INTEGRITY</div>
  </section>

</div>
</body>
</html>
```